VARNO - new private security company in Guyana, South America needs a website & logo design

New private security company in Guyana needs a website ready for the company launch. The business will offer armed and unarmed security to high net worth individuals, politicians, government officials, diplomats and off-shore oil industry vessels and platforms.

The company has its own heliport and indoor training range, armoured vehicles, ambulances and uniformed security personnel, and we would like some imager to indicate this.

The team leaders are all ex-special forces.

The website structure should be something like:

PAGE 1 Home
PAGE 2 About Us
PAGE 3 Guyana Security Overview
PAGE 4 Services
PAGE 5 Contact Us
PAGE 6 Useful Links

We have uploaded a file with the text copy for each of these pages.

The web domain has been registered through 456-dom and is www.varno.group

Target Market(s)

Corporations involved in the oil and gas industry, Embassies, Investment companies and individuals, Caribbean diaspora.

Industry/Entity Type

Security Service

Logo Text

VARNO

Coding

Coded - Design and coding required

Number of Pages Required

5+ page

Font styles to use
Sans Serif

Requirements
Must have
• Must have:
an enquiry/contact form page
general location map: https://mapz.example/loc/kP8wq2Lbnxv7hRt4;
text as per web content document uploaded to this site
Nice to have
• Images of private security (cars, bodyguards, helicopters/planes, etc)
Images of Maritime security (non-military)
Images of people of colour (Guyana has mainly afro and indian residents)
Image of a high tec security control room

```html
<!DOCTYPE html>
<html lang="en">
<head>
<meta charset="utf-8">
<title>VARNO Security — Home</title>
<link href="https://fonts.googleapis.com/css2?family=Oswald:wght@300;400;500;700&family=Lato:wght@400;700&display=swap" rel="stylesheet">
<style>
:root{
  --black:#000;
  --charcoal:#262727;
  --blue:#2a7bb8;
  --blue-bright:#2f8ad0;
  --white:#fff;
  --muted:#cfd6dc;
  --rule:#333;
}
*{box-sizing:border-box;margin:0;padding:0}
html,body{width:1200px;height:1200px;overflow:hidden;background:var(--white)}
body{position:relative;font-family:'Lato',sans-serif;color:var(--white)}
.page{position:absolute;left:326px;top:23px;width:683px;height:1442px;transform:scale(.8);transform-origin:0 0;background:var(--black);overflow:hidden}
.abs{position:absolute}
.heading{font-family:'Oswald',sans-serif;font-weight:400;text-transform:uppercase;letter-spacing:-.2px}
.underline{height:2px;width:40px;background:var(--blue-bright)}

/* nav */
.nav{left:0;top:0;width:683px;height:40px;background:var(--black)}
.brand-name{font-family:'Oswald',sans-serif;font-weight:700;line-height:1}
.brand-tag{font-family:'Oswald',sans-serif;font-weight:400;color:var(--blue-bright);letter-spacing:2px;line-height:1}
.nav .brand-name{left:64px;top:6px;font-size:18px}
.nav .brand-tag{left:64px;top:26px;font-size:7px}
.nav-links{left:300px;top:14px;display:flex;gap:13px;font-family:'Oswald',sans-serif;font-size:7px}
.nav-links .active{color:var(--blue-bright)}

/* hero */
.hero{left:0;top:40px;width:683px;height:267px;background:linear-gradient(100deg,#3b3f45 0%,#2a2d33 35%,#4a4a4e 60%,#33353a 100%)}
.hero-title{left:248px;top:86px;line-height:1.05}
.hero-title .l1{font-size:47px;font-weight:500;display:block}
.hero-title .l2{font-size:37px;font-weight:400;display:block}

/* intro */
.intro{left:0;top:307px;width:683px;height:355px;background:var(--charcoal)}
.intro-copy{left:64px;top:40px;width:242px;font-size:7px;line-height:13.5px}
.intro-copy p{margin-bottom:6px}
.why-title{left:360px;top:36px;font-size:26px;font-weight:300}
.why .underline{left:419px;top:76px}
.feature{left:382px;display:flex;align-items:center;gap:8px;font-size:9px;line-height:12px}
.feature svg{flex:none}

/* services */
.services{left:0;top:662px;width:348px;height:315px;background:var(--blue)}
.services h2{left:64px;top:82px;font-size:27px;font-weight:400}
.services .underline{left:116px;top:118px;background:var(--white)}
.services-copy{left:65px;top:136px;width:272px;font-size:7px;line-height:12px}
.services-copy p{margin-bottom:12px}
.services-copy .mail{color:#9fc6e6}
.btn{display:flex;align-items:center;justify-content:center;font-size:8px;font-weight:700;letter-spacing:.6px;text-transform:uppercase}
.btn-outline{left:64px;top:206px;width:123px;height:34px;border:2px solid var(--white)}
.tile{width:168px;height:157px;display:flex;align-items:center;justify-content:center;text-align:center;font-family:'Oswald',sans-serif;font-weight:500;font-size:10px;line-height:12px;letter-spacing:.3px;border:1px solid #1b1b1b}
.tile.wide span{font-size:11px;line-height:16px}

/* about */
.about{left:0;top:977px;width:683px;height:252px;background:linear-gradient(90deg,#2b2a29 0%,#1d1d1d 50%,#262626 100%)}
.about-photo{left:0;top:0;width:340px;height:252px;background:linear-gradient(120deg,#3a3330 0%,#1f1c1b 70%,#252525 100%)}
.about h2{left:352px;top:66px;font-size:27px;font-weight:400}
.about-copy{left:353px;top:117px;width:305px;font-size:7.5px;line-height:12px}
.btn-solid{left:352px;top:165px;width:123px;height:34px;background:var(--blue-bright)}

/* footer */
.footer{left:0;top:1229px;width:683px;height:213px;background:var(--black)}
.footer .brand-name{left:64px;top:30px;font-size:31px}
.footer .brand-tag{left:64px;top:65px;font-size:15px;letter-spacing:3px}
.footer-note{left:64px;top:97px;width:175px;font-size:7.5px;line-height:12px}
.footer-links{left:330px;top:32px;list-style:none;font-size:7.5px;line-height:12.6px}
.footer-links li::before{content:"";display:inline-block;width:3px;height:3px;border-radius:50%;background:var(--blue-bright);margin-right:6px;vertical-align:middle}
.contact{left:528px;display:flex;gap:6px;font-size:7.5px;line-height:12px}
.rule{left:64px;top:180px;width:555px;height:1px;background:var(--rule)}
.copyright{left:0;top:190px;width:683px;text-align:center;font-size:7.5px}
.copyright a{color:var(--blue-bright);text-decoration:none}
</style>
</head>
<body>
<div class="page">

  <header class="nav abs">
    <div class="brand-name abs">VARNO</div>
    <div class="brand-tag abs">SECURITY</div>
    <nav class="nav-links abs">
      <span class="active">Home</span><span>About Us</span><span>Guyana Security Overview</span><span>Services</span><span>Contact Us</span>
    </nav>
  </header>

  <section class="hero abs" role="img" aria-label="Security officer in cap and sunglasses standing arms crossed on a busy city street with a car and crowd behind">
    <h1 class="hero-title heading abs"><span class="l1">Security Solutions</span><span class="l2">For You &amp; Your Business</span></h1>
  </section>

  <section class="intro abs">
    <div class="intro-copy abs">
      <p>VARNO is a fully licensed Guyanese security company offering a wide range of security services to the public and private sector and is a unique collaboration of highly trained Guyanese operatives and elite British military security experts.</p>
      <p>Our combination of local knowledge, contacts and resources teamed with years of active service in some of the most hostile regions in the world and high threat environments creates a highly capable, responsive and professional security service.</p>
      <p>We have years of experience of delivering effective security solutions to high net worth individuals and their families, multi-national corporations, royalty, politicians and valuable state owned and private assets. We have developed the most advanced training offered to security personnel in Guyana, utilizing elite British operators and security doctrine and protocols developed over decades combined with a deep cultural understanding of the region.</p>
      <p>Our security operations are supported by the latest advanced technology and equipment and a wide-reaching intelligence network. Information, Technology, Training and Experience are the cornerstones of our operations.</p>
    </div>
    <div class="why">
      <h2 class="why-title heading abs">Why Choose Us?</h2>
      <div class="underline abs"></div>
    </div>
    <div class="feature abs" style="top:128px">
      <svg width="26" height="26" viewBox="0 0 26 26"><circle cx="13" cy="13" r="12" fill="#2f8ad0"/><path d="M8.5 13.5l3 3 6-6" stroke="#fff" stroke-width="2" fill="none"/></svg>
      <span>Fully Licensed<br>Security Company</span>
    </div>
    <div class="feature abs" style="top:186px">
      <svg width="26" height="26" viewBox="0 0 26 26"><circle cx="13" cy="13" r="12" fill="#2f8ad0"/><path d="M13 7l5 2v4c0 3-2 5-5 6-3-1-5-3-5-6V9z" fill="#fff"/></svg>
      <span>Responsive and Professional<br>Security Service</span>
    </div>
    <div class="feature abs" style="top:244px">
      <svg width="26" height="26" viewBox="0 0 26 26"><circle cx="13" cy="13" r="12" fill="#2f8ad0"/><path d="M9 18l3-6 4-3M12 12l3 2" stroke="#fff" stroke-width="2" fill="none" stroke-linecap="round"/></svg>
      <span>Most Advanced Training</span>
    </div>
    <div class="feature abs" style="top:301px">
      <svg width="26" height="26" viewBox="0 0 26 26"><circle cx="13" cy="13" r="12" fill="#2f8ad0"/><path d="M13 7l5 2v4c0 3-2 5-5 6-3-1-5-3-5-6V9z" fill="#fff"/><circle cx="13" cy="12.5" r="2" fill="#2f8ad0"/></svg>
      <span>Years of Active Service</span>
    </div>
  </section>

  <section class="services abs">
    <h2 class="heading abs">Our Services</h2>
    <div class="underline abs"></div>
    <div class="services-copy abs">
      <p>VARNO offers the following services to protect you, your colleagues, family, business or assets.</p>
      <p>Contact <span class="mail">ba@varno.group</span> for further information or to arrange a security consultation.</p>
    </div>
    <div class="btn btn-outline abs">All Services</div>
  </section>

  <div class="tile abs" style="left:348px;top:662px;background:linear-gradient(160deg,#2a2a2c,#1a1a1b)" role="img" aria-label="Suited bodyguard holding a handgun"><span>Unarmed and Armed Close<br>Protection</span></div>
  <div class="tile wide abs" style="left:516px;top:662px;width:167px;background:linear-gradient(180deg,#49525c,#5b5a55 70%,#6a6658)" role="img" aria-label="Helicopter flying over a landing pad"><span>Casevac<br>(Casualty Evacuation)</span></div>
  <div class="tile abs" style="left:348px;top:820px;background:linear-gradient(180deg,#3f4a52,#2a3640)" role="img" aria-label="Patrol boat speeding across water"><span>Maritime Security</span></div>
  <div class="tile abs" style="left:516px;top:820px;width:167px;background:linear-gradient(160deg,#3c4a35,#252a22)" role="img" aria-label="Security officer in uniform outdoors"><span>Static &amp; Mobile Security<br>(Armed and Unarmed)</span></div>

  <section class="about abs">
    <div class="about-photo abs" role="img" aria-label="Security officer speaking into a radio, seen from behind"></div>
    <h2 class="heading abs">Who We Are</h2>
    <p class="about-copy abs">VARNO Security teams are fully licensed by the Guyanese Police Force to offer armed and unarmed security services and all service weapons and ammunition are controlled and maintained in full compliance with Guyanese regulations.</p>
    <div class="btn btn-solid abs">Learn More</div>
  </section>

  <footer class="footer abs">
    <div class="brand-name abs">VARNO</div>
    <div class="brand-tag abs">SECURITY</div>
    <p class="footer-note abs">VARNO is a Trading Division of Kaietur Holdings Inc, a duly incorporated and registered Guyanese corporation with Company Registration Number XXXXX and located at XXXXXXXXX.</p>
    <ul class="footer-links abs">
      <li>Home</li><li>About Us</li><li>Guyana Security Overview</li><li>Services</li><li>Contact Us</li><li>Useful Links</li>
    </ul>
    <div class="contact abs" style="top:34px">
      <svg width="13" height="16" viewBox="0 0 13 16"><path d="M6.5 0C3 0 0 2.7 0 6.2 0 10.5 6.5 16 6.5 16S13 10.5 13 6.2C13 2.7 10 0 6.5 0z" fill="#2f8ad0"/><circle cx="6.5" cy="6" r="2.3" fill="#000"/></svg>
      <span>88 Water Street<br>Kingsford, GY 40218</span>
    </div>
    <div class="contact abs" style="top:78px">
      <svg width="15" height="14" viewBox="0 0 15 14"><path d="M0 6L15 0 11 14 7 9z" fill="#2f8ad0"/></svg>
      <span>ba@varno.group</span>
    </div>
    <div class="contact abs" style="top:110px">
      <svg width="14" height="14" viewBox="0 0 14 14"><path d="M3 0l3 3-2 2c1 2 3 4 5 5l2-2 3 3-2 3C6 14 0 8 0 3z" fill="#2f8ad0"/></svg>
      <span>+1 (555) 014-2290</span>
    </div>
    <div class="rule abs"></div>
    <p class="copyright abs">© 2020 VARNO. All Rights Reserved. <a>Terms.</a> <a>Privacy Policy.</a></p>
  </footer>

</div>
</body>
</html>
```